Plumbing business card and logo desgin

Need a new business card and logo for a plumbing business based in Warragul, Australia. Business name is 9Brook plumbing & air-conditioning. We service all plumbing and gasfitting needs and installation of air-conditioning. We clear blocked drains, install new hot water systems, central heating, new and existing homes, roofing, sanitary and drainage.
i would like to have a space on there for website, email, phone, licence number and what we do as a company.
i would like a water droplet to be incorporated into the design to try and stand out that we are a plumbing business

Contact Information for Business Card

phone number: 0497215836
Licence Number: 873614

Logo Text

9Brook Plumbing & Air-Conditioning

```html
<!DOCTYPE html>
<html lang="en">
<head>
<meta charset="utf-8">
<title>9Brook Plumbing &amp; Air-Conditioning – Business Card</title>
<link rel="stylesheet" href="https://fonts.googleapis.com/css2?family=Roboto+Condensed:wght@300;400&display=swap">
<style>
  :root {
    --page: #ffffff;
    --card-white: #ffffff;
    --brand-blue: #1a8fd0;
    --blue-light: #1bb0e6;
    --blue-mid: #0c98d6;
    --blue-deep: #0672b0;
    --pipe-tint: #3aaee3;
    --ink: #1a1a1a;
    --on-blue: #ffffff;
  }
  * { margin: 0; padding: 0; box-sizing: border-box; }
  html, body {
    width: 1200px; height: 848px; overflow: hidden;
    background: var(--page);
    font-family: "Roboto Condensed", "Arial Narrow", sans-serif;
  }
  .sheet { position: relative; width: 1200px; height: 848px; }

  .card {
    position: absolute; top: 294px;
    width: 364px; height: 203px;
    border-radius: 20px; overflow: hidden;
  }
  .card--front { left: 197px; background: var(--card-white); border: 1px solid #e6e6e6; }
  .card--back {
    left: 605px;
    background: linear-gradient(180deg, var(--blue-light) 0%, var(--blue-mid) 50%, var(--blue-deep) 100%);
  }

  /* Front: decorative pipe band area */
  .pipe-decor {
    position: absolute; left: 0; top: 0; width: 124px; height: 100%;
    background: linear-gradient(160deg, var(--pipe-tint) 0%, #7cc9ee 55%, #c4e7f8 100%);
    opacity: 0.85;
  }

  /* Back: droplet texture area */
  .droplet-field {
    position: absolute; inset: 0;
    background:
      radial-gradient(ellipse at 30% 30%, rgba(255,255,255,0.22), rgba(255,255,255,0) 55%),
      radial-gradient(ellipse at 80% 70%, rgba(255,255,255,0.14), rgba(255,255,255,0) 50%);
  }
  .brand-mark {
    position: absolute; left: 712px; top: 364px;
    width: 60px; height: 60px; border-radius: 50%;
    background: rgba(255,255,255,0.85);
  }

  .brand { position: absolute; }
  .card--front .brand { left: 179px; top: 31px; }
  .card--back .brand { left: 204px; top: 66px; }
  .brand__name {
    font-weight: 400; font-size: 28px; line-height: 1;
    letter-spacing: 0.2px; color: var(--brand-blue);
  }
  .brand__tagline {
    margin-top: 3px; font-weight: 300; font-size: 15px; line-height: 18px; color: var(--ink);
  }
  .card--back .brand__name,
  .card--back .brand__tagline { color: var(--on-blue); }

  .details {
    position: absolute; left: 179px; top: 120px;
    font-weight: 400; font-size: 10px; line-height: 12.5px;
    letter-spacing: 0.6px; color: var(--ink);
  }
  .details__web { margin-top: 13px; }
</style>
</head>
<body>
<main class="sheet">
  <section class="card card--front">
    <div class="pipe-decor" role="img" aria-label="Decorative blue pipe-elbow shapes along the left edge"></div>
    <div class="brand">
      <div class="brand__name">9BROOK</div>
      <div class="brand__tagline">Plumbing &amp;<br>Air-Conditioning</div>
    </div>
    <div class="details">
      <div>Lic. Number: 873614</div>
      <div>Contact: 0497215836</div>
      <div class="details__web">www.9brookplumbing.com</div>
    </div>
  </section>

  <section class="card card--back">
    <div class="droplet-field" role="img" aria-label="Water droplets scattered across a blue surface"></div>
    <div class="brand">
      <div class="brand__name">9BROOK</div>
      <div class="brand__tagline">Plumbing &amp;<br>Air-Conditioning</div>
    </div>
  </section>
  <div class="brand-mark" aria-hidden="true"></div>
</main>
</body>
</html>
```